Billboard Design for Equipment Rental Business

We need a billboard design for our equipment rental business called Brevard Machinery Company. We are based in Georgia. We rent construction tools, equipment, and dumpsters. We currently have a design but feel like we could get something better. Our phone number is 912-307-5186 and our website is www.brevardmachinery-example.com

```html
<!DOCTYPE html>
<html lang="en">
<head>
<meta charset="utf-8">
<title>Brevard Machinery Company – Billboard</title>
<link href="https://fonts.googleapis.com/css2?family=Oswald:wght@500;600;700&display=swap" rel="stylesheet">
<style>
  :root {
    --hazard-yellow: #f6b91c;
    --hazard-black: #1c1a1b;
    --panel-white: #f1f1f3;
    --text-white: #ffffff;
    --stage: #d6d6d6;
  }
  * { margin: 0; padding: 0; box-sizing: border-box; }
  html, body {
    width: 1000px;
    height: 1200px;
    overflow: hidden;
    background: var(--stage);
    font-family: "Oswald", "Arial Narrow", sans-serif;
  }
  .billboard {
    position: absolute;
    left: 40px;
    top: 357px;
    width: 920px;
    height: 486px;
    overflow: hidden;
    background: repeating-linear-gradient(
      45deg,
      var(--hazard-black) 0 17px,
      var(--hazard-yellow) 17px 34px
    );
  }
  .brand-panel {
    position: absolute;
    left: 28px;
    top: 28px;
    width: 478px;
    height: 168px;
    background: var(--hazard-yellow);
    display: flex;
    align-items: center;
    padding-left: 28px;
    gap: 22px;
  }
  .brand-mark {
    width: 26px;
    height: 26px;
    background: var(--hazard-black);
    flex: none;
  }
  .brand-name {
    color: var(--hazard-black);
    font-weight: 700;
    line-height: 1;
  }
  .brand-name .primary {
    display: block;
    font-size: 64px;
    letter-spacing: 1px;
  }
  .brand-name .secondary {
    display: block;
    font-size: 18px;
    letter-spacing: 4.6px;
    margin-top: 4px;
  }
  .services-panel {
    position: absolute;
    left: 28px;
    top: 196px;
    width: 478px;
    height: 168px;
    background: var(--panel-white);
    display: flex;
    flex-wrap: wrap;
    justify-content: center;
    align-content: center;
    column-gap: 26px;
    row-gap: 18px;
  }
  .service {
    display: flex;
    align-items: center;
    gap: 12px;
    font-weight: 600;
    font-size: 38px;
    line-height: 1;
    color: var(--hazard-black);
    letter-spacing: 0.3px;
  }
  .service-icon {
    width: 50px;
    height: 50px;
    background: var(--hazard-yellow);
    display: flex;
    align-items: center;
    justify-content: center;
  }
  .service-icon svg { width: 34px; height: 34px; }
  .machine-visual {
    position: absolute;
    left: 500px;
    top: 10px;
    width: 390px;
    height: 370px;
    border-radius: 40% 18% 22% 30%;
    background: radial-gradient(ellipse at 55% 55%, #f2c245 0%, #d9a22a 45%, #5a4a2a 80%, rgba(28,26,27,0) 100%);
  }
  .contact-bar {
    position: absolute;
    left: 28px;
    top: 364px;
    width: 864px;
    height: 92px;
    background: var(--hazard-black);
    display: flex;
    align-items: center;
    padding-left: 40px;
  }
  .phone {
    display: flex;
    align-items: center;
    gap: 14px;
    color: var(--hazard-yellow);
    font-weight: 600;
    font-size: 54px;
    line-height: 1;
  }
  .phone svg { width: 40px; height: 40px; }
  .divider {
    width: 3px;
    height: 46px;
    background: var(--text-white);
    transform: skewX(-28deg);
    margin: 0 36px 0 34px;
  }
  .website {
    font-weight: 500;
    font-size: 27px;
    color: var(--text-white);
    letter-spacing: 0.4px;
  }
  .website .domain { color: var(--hazard-yellow); }
</style>
</head>
<body>
  <main class="billboard">
    <section class="brand-panel">
      <span class="brand-mark" aria-hidden="true"></span>
      <h1 class="brand-name">
        <span class="primary">BREVARD</span>
        <span class="secondary">MACHINERY COMPANY</span>
      </h1>
    </section>

    <section class="services-panel">
      <div class="service">
        <span class="service-icon">
          <svg viewBox="0 0 34 34" fill="none" stroke="#1c1a1b" stroke-width="2.4" stroke-linecap="round">
            <path d="M7 27 L22 12"/>
            <path d="M22 12 a5 5 0 1 1 4 -6 l-4 4 2 2 4 -4 a5 5 0 0 1 -6 4"/>
            <path d="M8 7 L27 26"/>
            <path d="M5 5 l4 0 0 4"/>
          </svg>
        </span>
        TOOLS
      </div>
      <div class="service">
        <span class="service-icon">
          <svg viewBox="0 0 34 34" fill="none" stroke="#1c1a1b" stroke-width="2.2" stroke-linejoin="round">
            <rect x="5" y="24" width="20" height="5" rx="2.5"/>
            <rect x="8" y="16" width="11" height="8"/>
            <path d="M19 18 L25 8 L30 14 L29 20"/>
          </svg>
        </span>
        EQUIPMENT
      </div>
      <div class="service">
        <span class="service-icon">
          <svg viewBox="0 0 34 34" fill="none" stroke="#1c1a1b" stroke-width="2.2" stroke-linejoin="round">
            <path d="M6 11 H28 L26 27 H8 Z"/>
            <path d="M5 8 H29"/>
            <path d="M12 14 V24 M17 14 V24 M22 14 V24"/>
            <circle cx="10" cy="29.5" r="1.5"/>
            <circle cx="24" cy="29.5" r="1.5"/>
          </svg>
        </span>
        DUMPSTERS
      </div>
    </section>

    <div class="machine-visual" role="img" aria-label="Photo of a yellow tracked excavator with its bucket lowered"></div>

    <footer class="contact-bar">
      <div class="phone">
        <svg viewBox="0 0 40 40" fill="none" stroke="#ffffff" stroke-width="2.4" stroke-linecap="round" stroke-linejoin="round">
          <path d="M10 6 l6 7 -3 4 c2 4 5 7 9 9 l4 -3 7 6 -4 5 c-12 0 -23 -11 -23 -23 z"/>
          <path d="M24 6 a10 10 0 0 1 10 10"/>
          <path d="M23 11 a5 5 0 0 1 6 5"/>
        </svg>
        <span class="phone-number">912-307-5186</span>
      </div>
      <span class="divider" aria-hidden="true"></span>
      <div class="website">www.<span class="domain">brevardmachinery-example</span>.com</div>
    </footer>
  </main>
</body>
</html>
```